Velvet Harbour - R&B Band in Sydney Requires new Business Cards

We're a 6 piece R&B Soul band in Sydney called Velvet Harbour that requires new promotional material including Business Cards.

We are very well known around Sydney and have a resident venue gig at the Marlowe Grand Sydney hotel. We play predominantly old & new school R&B hits.

Our logo is attached, colours are Brown & yellow.
Initial idea was to get sugar packets made up with our logo and contact details.

```html
<!DOCTYPE html>
<html lang="en">
<head>
<meta charset="utf-8">
<title>Velvet Harbour — Business Cards</title>
<link rel="stylesheet" href="https://fonts.googleapis.com/css2?family=Fredoka:wght@500;700&display=swap">
<style>
  :root {
    --bg: #d9d6d0;
    --brown: #4a2c0c;
    --brown-deep: #3a2208;
    --yellow: #f5dc3a;
    --yellow-light: #f9e86a;
    --ink: #4a2c0c;
  }
  * { margin: 0; padding: 0; box-sizing: border-box; }
  html, body { width: 1200px; height: 1200px; overflow: hidden; }
  body {
    background: var(--bg);
    font-family: "Fredoka", "Arial Rounded MT Bold", sans-serif;
    display: flex;
    flex-direction: column;
    align-items: center;
    justify-content: center;
    gap: 80px;
  }
  .card {
    width: 840px;
    height: 480px;
    border-radius: 6px;
    box-shadow: 0 18px 40px rgba(0,0,0,0.28);
    position: relative;
    overflow: hidden;
  }

  /* Front: band name */
  .card--front {
    background: linear-gradient(135deg, var(--brown) 0%, var(--brown-deep) 100%);
    display: flex;
    align-items: center;
    justify-content: center;
  }
  .band-name {
    display: flex;
    align-items: center;
    gap: 26px;
    color: var(--yellow);
    font-weight: 700;
    font-size: 92px;
    line-height: 0.95;
    text-transform: uppercase;
    letter-spacing: 2px;
  }
  .band-name__dot {
    width: 46px;
    height: 46px;
    border-radius: 50%;
    background: var(--yellow);
    flex: none;
  }

  /* Back: contact */
  .card--back {
    background: linear-gradient(135deg, var(--yellow) 0%, var(--yellow-light) 55%, var(--yellow) 100%);
    color: var(--ink);
  }
  .contact {
    position: absolute;
    left: 80px;
    top: 120px;
    width: 690px;
  }
  .guitar {
    position: absolute;
    right: 80px;
    top: 92px;
    width: 300px;
    height: 64px;
  }
  .person {
    display: flex;
    align-items: flex-end;
    font-weight: 700;
    text-transform: uppercase;
    line-height: 0.9;
  }
  .person__first { font-size: 104px; letter-spacing: 1px; }
  .person__last { font-size: 104px; margin-left: 18px; transform: translateY(62px); }
  .details-row {
    display: flex;
    align-items: baseline;
    gap: 14px;
    margin-top: -6px;
  }
  .role {
    font-weight: 700;
    font-size: 50px;
    line-height: 1;
  }
  .phone {
    font-weight: 700;
    font-size: 44px;
    letter-spacing: 2px;
    margin-left: auto;
    transform: translateY(58px);
  }
  .email {
    font-weight: 500;
    font-style: italic;
    font-size: 36px;
    margin-top: 4px;
    margin-left: 20px;
  }
  .web {
    font-weight: 500;
    font-size: 36px;
    margin-left: 20px;
  }
</style>
</head>
<body>
  <section class="card card--front" aria-label="Business card front">
    <div class="band-name">
      <span class="band-name__dot"></span>
      <span>Velvet<br>Harbour</span>
    </div>
  </section>

  <section class="card card--back" aria-label="Business card back">
    <svg class="guitar" role="img" aria-label="Illustration of an electric guitar" viewBox="0 0 300 64">
      <rect x="0" y="0" width="300" height="64" rx="10" fill="#4a2c0c" opacity="0.85"/>
    </svg>
    <div class="contact">
      <div class="person">
        <span class="person__first">Sam</span>
        <span class="person__last">Reyes</span>
      </div>
      <div class="details-row">
        <span class="role">guitarist</span>
        <span class="phone">011 555 0192</span>
      </div>
      <div class="email">sam@velvetharbour.com</div>
      <div class="web">www.velvetharbour.com</div>
    </div>
  </section>
</body>
</html>
```